Railroad Association needs One-Page Infographic

Please see attachment for text and graphic. email with questions please. This piece will be handed out to legislators and state officials.

Target Market(s)

state legislature. state officials

Font styles to use
Serif

Colors
ec1f27

Requirements
Must have
• The graphic needs to be done right. Please email me with any questions.

```html
<!DOCTYPE html>
<html lang="en">
<head>
<meta charset="utf-8">
<title>Crossing Railroad Right of Way – Flyer</title>
<link href="https://fonts.googleapis.com/css2?family=Fira+Sans:ital,wght@0,500;0,700;0,800;1,700&family=Source+Sans+3:wght@400;700&display=swap" rel="stylesheet">
<style>
:root{
  --red:#ec1f27;
  --red-deep:#b5121b;
  --red-dark:#7d0f15;
  --navy:#1b2a4a;
  --sky:#e6f4fa;
  --sand:#e3cc98;
  --pink:#fbd3d5;
  --paper:#ffffff;
  --stage:#e9e9e9;
  --ink-grey:#555;
}
*{margin:0;padding:0;box-sizing:border-box}
html,body{width:1200px;height:1200px;overflow:hidden}
body{background:var(--stage);font-family:"Source Sans 3",sans-serif;position:relative}
.page{position:absolute;top:162px;width:516px;height:730px;overflow:hidden;box-shadow:0 10px 24px rgba(0,0,0,.18)}
.page--front{left:57px;background:var(--sky)}
.page--back{left:626px;background:linear-gradient(160deg,#e21d26 0%,#b5121b 55%,#7d0f15 100%)}

/* front */
.banner{position:absolute;left:0;top:0;width:516px;height:93px}
.banner__title{position:absolute;left:0;top:31px;width:436px;text-align:center;font-family:"Fira Sans",sans-serif;font-weight:700;font-size:22px;color:#fff;letter-spacing:.2px}
.banner__sub{position:absolute;left:0;top:71px;width:436px;text-align:center;font-family:"Fira Sans",sans-serif;font-weight:700;font-size:13px;color:var(--ink-grey)}
.scene{position:absolute;left:0;top:134px;width:516px;height:270px;background:linear-gradient(180deg,var(--sand) 0%,#f0dfc6 45%,var(--pink) 75%,var(--red-deep) 100%)}
.process{position:absolute;left:0;top:398px;width:516px;height:272px;background:linear-gradient(180deg,var(--red-deep),#a3121a)}
.process__title{position:absolute;left:0;top:-52px;width:370px;text-align:center;font-family:"Fira Sans",sans-serif;font-weight:800;font-size:32px;letter-spacing:3px;color:#fff}
.steps{position:absolute;left:26px;top:22px;width:300px;list-style:none}
.step{display:flex;align-items:center;height:60px}
.step__num{width:42px;font-family:"Fira Sans",sans-serif;font-weight:700;font-size:50px;line-height:1;color:#fff}
.step__text{font-size:11.5px;line-height:1.1;color:#fff}
.step__text b{font-weight:700}
.sign{position:absolute;left:311px;top:36px;width:175px;height:175px;background:linear-gradient(135deg,#fff,#ececec);transform:rotate(1deg);padding:26px 14px;text-align:center;color:var(--navy);font-size:15px;line-height:1.05;box-shadow:0 2px 5px rgba(0,0,0,.25)}
.sign b{font-weight:700}
.sign__post{position:absolute;left:393px;top:211px;width:8px;height:34px;background:#b9a98a}
.footnote{position:absolute;left:0;top:670px;width:516px;height:60px;background:var(--red);padding:15px 26px;color:#fff;font-size:7.6px;line-height:1.25}

/* back */
.track-deco{position:absolute;left:0;top:0}
.back__title{position:absolute;left:130px;top:113px;font-family:"Fira Sans",sans-serif;font-weight:700;font-size:23px;line-height:1.12;color:#fff}
.back__title i{font-style:italic}
.keys{position:absolute;left:152px;top:258px;list-style:none}
.key{display:flex;align-items:center;height:47px;font-family:"Fira Sans",sans-serif;font-weight:700;font-size:24px;color:#fff}
.key svg{width:36px;height:36px;margin-right:22px}
.brand{position:absolute;left:31px;top:630px;width:130px;font-family:"Fira Sans",sans-serif;font-weight:700;font-size:15px;line-height:1.15;color:#fff}
.call{position:absolute;right:29px;top:644px;text-align:right;color:#fff;font-family:"Fira Sans",sans-serif;font-weight:700}
.call__label{font-size:12.5px}
.call__phone{font-size:24px;line-height:1.1}
</style>
</head>
<body>

<section class="page page--front">
  <div class="scene" role="img" aria-label="Illustration of a railroad track crossing a highway between sand hills, with a broadband expansion line, a railroad right of way marker and an association sign on a grassy red hill"></div>

  <svg class="banner" viewBox="0 0 516 93" aria-hidden="true">
    <rect x="0" y="30" width="440" height="37" fill="var(--red)"/>
    <polygon points="436,0 516,47 436,93" fill="var(--red)"/>
    <rect x="0" y="67" width="436" height="26" fill="#fff"/>
  </svg>
  <h1 class="banner__title">CROSSING RAILROAD RIGHT OF WAY</h1>
  <p class="banner__sub">WHAT IS THE PROCESS?</p>

  <div class="process">
    <h2 class="process__title">PROCESS</h2>
    <ol class="steps">
      <li class="step"><span class="step__num">1</span><span class="step__text">Contact <b>Railroad</b> to obtain application<br>and specifications.</span></li>
      <li class="step"><span class="step__num">2</span><span class="step__text">Submit application to <b>Railroad</b><br>with engineering plans.</span></li>
      <li class="step"><span class="step__num">3</span><span class="step__text">When plans are approved, enter into<br>License Agreement with <b>Railroad</b>.</span></li>
      <li class="step"><span class="step__num">4</span><span class="step__text">With <b>Railroad Safety Protocols</b> and<br><b>approved</b> work plan in place, coordinate<br>with operations to obtain flagman.</span></li>
    </ol>
    <div class="sign__post"></div>
    <div class="sign"><b>Every Railroad company</b> has a detailed process to ensure <b>SAFETY</b> and avoid interruption to operations when crossing railroad ROW.</div>
  </div>

  <p class="footnote">Railroads ad here to strict safety and notification standards so that both the entity creating an encumbrance on railroad property as well as the railroads themselves, establish clear rules of engagement that allow each to accomplish their own goals while minimizing risk to the public.</p>
</section>

<section class="page page--back">
  <svg class="track-deco" width="516" height="730" viewBox="0 0 516 730" role="img" aria-label="Faint decorative railroad track curving down the left side and across the bottom">
    <path d="M22 0 H125 V520 Q150 620 250 610 H516 V670 H240 Q80 660 22 560 Z" fill="#9e0d14" opacity=".35"/>
  </svg>

  <h2 class="back__title">KEYS TO A <i>SAFE</i> AND<br>THOROUGH PROCESS</h2>

  <ul class="keys">
    <li class="key"><svg viewBox="0 0 36 36" fill="none" stroke="#fff" stroke-width="3.5" stroke-linejoin="round"><path d="M17 6H6v24h24V19"/><path d="M28 4l5 5-13 13h-5v-5z"/></svg>Plan</li>
    <li class="key"><svg viewBox="0 0 36 36" fill="none" stroke="#fff" stroke-width="4"><path d="M7 17a11 11 0 0 1 20-6"/><path d="M29 19a11 11 0 0 1-20 6"/><path d="M28 3v9h-9M8 33v-9h9" stroke-width="3.5"/></svg>Review</li>
    <li class="key"><svg viewBox="0 0 36 36"><path d="M5 4h26v22H20l-4 7-4-7H5z" fill="#fff"/></svg>Communicate</li>
    <li class="key"><svg viewBox="0 0 36 36" fill="none" stroke="#fff" stroke-width="3.5" stroke-linejoin="round"><path d="M22 5H5v27h27V17"/><path d="M11 17l6 6L33 6"/></svg>Agree</li>
    <li class="key"><svg viewBox="0 0 36 36" fill="#fff"><ellipse cx="18" cy="8" rx="15" ry="5"/><path d="M3 12c0 3 7 5 15 5s15-2 15-5v6c0 3-7 5-15 5S3 21 3 18z"/><path d="M3 22c0 3 7 5 15 5s15-2 15-5v6c0 3-7 5-15 5S3 31 3 28z"/></svg>Install</li>
  </ul>

  <p class="brand">Great Lakes Rail Council</p>
  <div class="call">
    <p class="call__label">CALL US NOW AT</p>
    <p class="call__phone">555 014 2736</p>
  </div>
</section>

</body>
</html>
```